Qortvax@mailvane.net

I am making this a landing page and I want to really grab the person and get them to call. So, I want some up front language at the top language about why they should contact me right away. The person looking is in a tough spot, they woe a lot of debt, they do not want to file a bankruptcy for moral or personal reasons, I want them to know that bankruptcy is a legal process that can help them and that they should not fear checking out their options. I will give them all of the information and if they want to go further fine, if not, they will have a lot more information about their situation and options

The language at the top, I want to be

Thanks for visiting us. You came here because you are having debt problems and you want solutions. Yes, we want your business. But, we don't want it if it is not right for you. We have been at this a long time and assisted thousands of Hawaii people and families with their debt problems. Many of those people were referred by former clients, but, our biggest referral source is people who did not file a bankruptcy. The reason is simple- our absolutely free and confidential consultation will help you get a handle on your whole situation. We will discuss your assets, your debts, your income and expenses and get a complete picture. It is only with this complete global picture of your particular situation that you can know your options, all of them, and then you can decide what is right for you. You are the driver. Call us at 472-3000 (from all islands) and let us help you today!

The color should be calming without being wimpy.

i want the top to be simple and a call to action giving people the sense that we know what we are doing and that they can call us for truly no obligation and we can help them diagnose their money issues and I can give them their options and they can do whatever they wish with them.

Hawaii people between ages of 28-70 who have credit card, loan or mortgage problems and need a way to get out of their debt

Legal

• Must incorporate the items at plkwindra.com. May be helpful to look at owezerozumbo.com for example of the "clean clear" landing I would like to "grab" the customer's attention and get them to call me, phone is better than email. So must have contact us too.

```html
<!DOCTYPE html>
<html lang="en">
<head>
<meta charset="utf-8">
<title>Dorian K. Welham – Hawaii Bankruptcy Attorney</title>
<link href="https://fonts.googleapis.com/css2?family=Arimo:wght@400;700&family=Oswald:wght@500&family=Lora:wght@400&display=swap" rel="stylesheet">
<style>
:root{
  --navy:#0c3553;
  --navy-deep:#06233a;
  --blue:#1a5c8a;
  --orange:#f39a1c;
  --orange-light:#ffc84a;
  --accent:#ff6a00;
  --beige:#efe2cb;
  --ink:#2a2a2a;
  --muted:#444;
  --footer:#07192a;
  --white:#fff;
}
*{box-sizing:border-box;margin:0;padding:0}
html,body{width:882px;height:1200px;overflow:hidden}
body{position:relative;background:var(--beige);font-family:"Arimo",Arial,sans-serif;color:var(--ink)}
.abs{position:absolute}

/* header */
.site-header{left:0;top:0;width:882px;height:121px;background:radial-gradient(ellipse at 55% 40%,#2a6fa0 0%,#134a72 45%,var(--navy-deep) 100%)}
.brand{left:98px;top:50px;display:flex;align-items:center;gap:8px;font-family:"Arimo",Arial,sans-serif;font-weight:700;font-size:19px;color:var(--white);white-space:nowrap}
.brand .mark{width:14px;height:14px;background:var(--orange)}
.tagline{left:348px;top:33px;color:var(--white);font-weight:700;font-size:14px;line-height:15px;letter-spacing:-.3px}
.header-phone{left:346px;top:64px;color:var(--white);font-weight:700;font-size:24px}
.header-photo{left:655px;top:4px;width:130px;height:117px;background:linear-gradient(180deg,#26313b,#0e1720);border-radius:40px 40px 0 0}

/* nav band */
.nav-band{left:0;top:121px;width:882px;height:91px;background:linear-gradient(180deg,var(--orange-light) 0%,var(--orange) 55%,#f47b12 100%);border-bottom:5px solid #16283a}
.main-nav{left:199px;top:131px;display:flex;font-family:"Oswald",sans-serif;font-size:16px;text-transform:uppercase}
.main-nav a{color:#1b1b1b;text-decoration:none;padding:3px 8px;margin-right:16px}
.main-nav a.current{background:#13273a;color:var(--white)}

/* intro panel */
.intro-panel{left:98px;top:168px;width:686px;height:454px;background:var(--white);border-radius:3px;box-shadow:0 1px 3px rgba(0,0,0,.15)}
.panel-shadow{left:160px;top:622px;width:560px;height:8px;background:radial-gradient(ellipse at top,rgba(0,0,0,.35),transparent 70%)}
.title-bar{left:119px;top:190px;width:644px;height:39px;background:linear-gradient(180deg,#1d5b86,var(--navy-deep));color:var(--white);font-weight:700;font-size:21px;padding:7px 14px;letter-spacing:-.4px}
.intro-text{left:119px;top:244px;width:648px;font-size:10.9px;line-height:13.8px;color:#333}
.intro-text .call{color:var(--accent);font-weight:700}

.hero-frame{left:120px;top:354px;width:408px;height:245px;background:#d9d9d9;padding:6px}
.hero-photo{width:100%;height:100%;background:linear-gradient(120deg,#a9a39a 0%,#5e4a3e 45%,#8c7a6a 70%,#c8c0b4 100%);position:relative}
.hero-caption{position:absolute;left:0;top:94px;width:222px;height:139px;background:rgba(70,70,70,.55);color:var(--white);font-family:"Lora",Georgia,serif;font-size:13px;line-height:15px;padding:20px 16px}
.hero-caption p+p{margin-top:12px;font-size:11.5px}

.consult{left:549px;top:352px;width:214px}
.consult h2{background:linear-gradient(180deg,#1d5b86,var(--navy-deep));color:var(--white);font-weight:400;font-size:16px;height:33px;padding:7px 13px}
.consult .lead{font-size:9px;line-height:11px;color:#333;margin-top:12px}
.consult .lead b{color:var(--navy)}
.field{display:flex;justify-content:space-between;margin-top:7px;font-size:8.5px;line-height:9px;color:#444}
.field .box{width:142px;height:22px;background:#d6d6d6;border:1px solid #bbb}
.field .box.tall{height:47px}
.form-foot{display:flex;justify-content:space-between;align-items:center;margin-top:14px;padding-left:8px}
.form-foot a{font-size:7.5px;color:#222}
.submit{width:76px;height:22px;background:linear-gradient(180deg,#ffb02a,#f27a10);color:#1a1a1a;font-size:12px;text-align:center;line-height:22px}

/* lower content */
.links-box{left:98px;top:645px;width:458px;height:256px;background:var(--white);border-radius:3px;box-shadow:0 1px 3px rgba(0,0,0,.2)}
.col-divider{left:321px;top:660px;width:1px;height:226px;background:#ccc}
.link-group{width:178px}
.link-group h3{font-weight:400;font-size:16px;color:var(--navy);padding-bottom:4px;border-bottom:1px solid #bbb;margin-bottom:8px}
.link-group ul{list-style:none;font-size:7.8px;line-height:8.4px;color:#222}
.link-group li{position:relative;padding-left:10px;margin-bottom:4px}
.link-group li::before{content:"";position:absolute;left:0;top:2px;width:4px;height:4px;border-radius:50%;background:var(--navy)}
.cat-cols{display:flex;gap:8px}
.cat-cols ul{width:90px}

.family-photo{left:576px;top:645px;width:209px;height:67px;background:linear-gradient(90deg,#6b5a47,#3e3a33 50%,#8a8378)}
.serving{left:577px;top:719px;font-size:9.5px;color:#222}
.video{left:576px;top:743px;width:198px;height:182px;background:linear-gradient(135deg,#7a6a5a,#3a3430 60%,#1d1d1d)}
.video-bar{left:576px;top:902px;width:198px;height:23px;background:#111;border-top:3px solid #c00}

.testimonials-title{left:97px;top:916px;font-size:16px;font-weight:400;color:var(--navy);letter-spacing:-.3px}
.testimonials{left:97px;top:945px;width:460px;font-size:7.9px;line-height:9px;color:#222}
.testimonials p{margin-bottom:10px}
.more-btn{left:98px;top:1034px;width:127px;height:18px;background:linear-gradient(180deg,#ffb02a,#f27a10);font-size:7.5px;text-align:center;line-height:18px;color:#1a1a1a}

.contact-title{left:574px;top:939px;font-size:16px;font-weight:400;color:var(--navy)}
.map{left:574px;top:963px;width:95px;height:73px;background:linear-gradient(135deg,#eae6dc,#d7dccf);border:1px solid #bbb}
.contact-info{left:675px;top:962px;font-size:8.2px;line-height:9.6px;color:#222;font-style:normal}
.map-link{left:675px;top:1029px;font-size:7.5px;color:#222;text-decoration:underline}

/* footer */
.site-footer{left:0;top:1078px;width:882px;height:122px;background:var(--footer);border-top:4px solid var(--orange)}
.badge{left:99px;top:1103px;width:112px;height:76px;background:#f1ede4}
.like{left:539px;top:1104px;display:flex;align-items:center;gap:6px;font-size:7px;color:#ddd}
.like .btn{width:34px;height:14px;background:#eef0f4;color:#333;font-size:7px;text-align:center;line-height:14px;border:1px solid #ccc}
.follow{left:539px;top:1126px;display:flex;align-items:center;gap:5px;color:var(--white);font-size:11px}
.follow .sq{width:10px;height:10px;background:#4d79b5}
.footer-links{left:539px;top:1145px;font-size:7px;line-height:11px;color:var(--white)}
.footer-links .u{text-decoration:underline}
</style>
</head>
<body>

<header class="abs site-header"></header>
<div class="abs brand"><span class="mark"></span>Dorian K. Welham</div>
<div class="abs tagline">HAWAII BANKRUPTCY ATTORNEY<br>AND DEBT SOLUTIONS</div>
<div class="abs header-phone">Call: 808-472-3000</div>
<div class="abs header-photo" role="img" aria-label="Photo of a smiling attorney in a dark suit"></div>

<div class="abs nav-band"></div>
<nav class="abs main-nav">
  <a class="current" href="#">Home</a><a href="#">About Us</a><a href="#">Chapter 7</a><a href="#">Chapter 13</a><a href="#">Blog</a><a href="#">Contact Us</a>
</nav>

<section class="abs intro-panel"></section>
<div class="abs panel-shadow"></div>
<h1 class="abs title-bar">About Dorian K. Welham</h1>
<p class="abs intro-text">Thanks for visiting us. You came here because you are having debt problems and you want solutions. Yes, we want your business. But, we don't want it if it is not right for you. We have been at this a long time and assisted thousands of Hawaii people and families with their debt problems. Many of those people were referred by former clients, but, our biggest referral source is people who did not file a bankruptcy. The reason is simple- our absolutely free and confidential consultation will help you Get a handle on your whole situation. We will discuss your assets, your debts, your income and expenses and get a complete picture. It is only with this complete global picture of your particular situation that you can know your options, all of them, and than you can decide what is right for you. You are the driver. <span class="call">Call us at 472-3000</span> ( from all islands ) and let us help you today!</p>

<div class="abs hero-frame">
  <div class="hero-photo" role="img" aria-label="Photo of two happy women outdoors making peace signs">
    <div class="hero-caption">
      <p>No Collector calls,<br>no harassment, no debts<br>- Feels Great!</p>
      <p>Get The Feeling!<br>Feel what its like to be debt free!</p>
    </div>
  </div>
</div>

<form class="abs consult">
  <h2>Free Consultation</h2>
  <p class="lead">Fill out the form below for a free no obligation consultation, or <b>Call: 808-472-3000</b></p>
  <div class="field" style="margin-top:12px"><span>Your Name<br>(required)</span><span class="box"></span></div>
  <div class="field"><span>Your Email<br>(required)</span><span class="box"></span></div>
  <div class="field"><span>Your Phone<br>(required)</span><span class="box"></span></div>
  <div class="field"><span>Your Name<br>Message</span><span class="box tall"></span></div>
  <div class="form-foot"><a href="#">Read Our Privacy Statement</a><span class="submit">Submit</span></div>
</form>

<section class="abs links-box"></section>
<div class="abs col-divider"></div>
<div class="abs link-group" style="left:115px;top:656px">
  <h3>Recent Articles</h3>
  <ul>
    <li>What Is Lien Stripping in a Chapter 13 Hawaii Bankruptcy?</li>
    <li>What Is A Co-Debtor Stay in a Chapter 13 Hawaii Bankruptcy?</li>
    <li>What is Chapter 13 Bankruptcy in Hawaii?</li>
    <li>What is Chapter 7 Bankruptcy in Hawaii?</li>
    <li>What is a Hawaii bankruptcy estate?</li>
  </ul>
</div>
<div class="abs link-group" style="left:116px;top:775px">
  <h3>Recent Videos</h3>
  <ul>
    <li>Why a Chapter 13 needs to be Feasible.</li>
    <li>What happens to my tax return if I file bankruptcy?</li>
    <li>What can be done if your car is worth less than what you owe.</li>
    <li>What if my house is worth less than I owe?</li>
    <li>Co Debtor Stay</li>
  </ul>
</div>
<div class="abs link-group" style="left:348px;top:656px">
  <h3>Resources</h3>
  <ul>
    <li>Why shouldn't I consolidate my debt?</li>
    <li>What happens to my tax return if I file bankruptcy?</li>
    <li>What can be done if your car is worth less than what you owe.</li>
    <li>What if my house is worth less than I owe?</li>
    <li>Co Debtor Stay</li>
  </ul>
</div>
<div class="abs link-group" style="left:348px;top:776px">
  <h3>Categories</h3>
  <div class="cat-cols">
    <ul><li>Articles</li><li>bankruptcy</li><li>Bankruptcy Hawaii</li><li>Bankruptcy Honolulu</li><li>Bankruptcy oahu</li><li>Blog</li></ul>
    <ul><li>Blogroll</li><li>CARE</li><li>chapter 13</li><li>Chapter 13 Bankruptcy Hawaii</li></ul>
  </div>
</div>

<div class="abs family-photo" role="img" aria-label="Photo of a smiling family with a baby in front of a house"></div>
<div class="abs serving">Serving Hawaii Since 1995</div>
<div class="abs video" role="img" aria-label="Video still of the attorney speaking in his office"></div>
<div class="abs video-bar"></div>
<svg class="abs" style="left:658px;top:813px" width="32" height="22" viewBox="0 0 32 22"><rect width="32" height="22" rx="3" fill="rgba(0,0,0,.7)"/><path d="M12 5 L22 11 L12 17 Z" fill="#fff"/></svg>
<svg class="abs" style="left:590px;top:910px" width="60" height="10" viewBox="0 0 60 10"><path d="M0 0 L7 5 L0 10Z" fill="#aaa"/><path d="M24 3 H27 L31 0 V10 L27 7 H24Z" fill="#aaa"/></svg>
<div class="abs" style="left:646px;top:910px;font-size:7px;color:#ddd">0:00 / 0:00</div>

<h2 class="abs testimonials-title">Client Testimonials</h2>
<div class="abs testimonials">
  <p>"Thanks for the good news about R's plan.... I also want to say thank you for always treating my mother with consideration. Your mindfulness, acuity, and helpfulness will always be remembered..."--HT</p>
  <p>"Thank you for guiding me during this difficult period of my life. I was unfamiliar with bankruptcy and my experience with you was nothing but positive..."--RK</p>
  <p>"I never thought in a million years I would have to even consider bankruptcy... Mr. Welham made it as painless as possible and I would highly recommend him to anyone. Thanks Dorian!"--TS</p>
</div>
<div class="abs more-btn">Click here for more testimonials...</div>

<h2 class="abs contact-title">Contact Info</h2>
<div class="abs map" role="img" aria-label="Small street map of the office location in Honolulu"></div>
<address class="abs contact-info">Dorian K. Welham,<br>Attorney-at-Law<br>2240 Mapleview St. Suite 1400<br>Honolulu, HI 96813<br>808-472-3000<br>info@plkwindra.com</address>
<a class="abs map-link" href="#">View larger map and directions</a>

<footer class="abs site-footer"></footer>
<div class="abs badge" role="img" aria-label="Professional association membership badge"></div>
<div class="abs like"><span class="btn">Like</span><span>Be the first of your friends to like this.</span></div>
<div class="abs follow">Follow Us On: <span class="sq"></span><span class="sq"></span><span class="sq" style="background:#c9413a"></span></div>
<div class="abs footer-links">
  Home -- About Us -- Chapter 7 -- Chapter 13 -- Blog -- Contact Us<br>
  <span class="u">Site Map</span>, <span class="u">Privacy Statement</span>, <span class="u">Terms of Service</span><br>
  © 2011 Dorian K. Welham. All rights reserved.
</div>

</body>
</html>
```